Brookside Grocer

Hope all is well!

Wanted to make business cards for my father. His name is Faisal Qureshi and owns convenience stores. I have attached logo :)

He does not want any title just simple name and phone. An email would be nice as well.

Faisal Qureshi
Cell: 413-585-2046
Store: 413-719-4820

Brooksidegrocer512@fernpost.com

The design and style is totally up to you :) The colors we were looking for were the same as logo :)

```html
<!DOCTYPE html>
<html lang="en">
<head>
<meta charset="UTF-8">
<title>Brookside Grocer – Business Card</title>
<link rel="stylesheet" href="https://fonts.googleapis.com/css2?family=Alegreya:wght@400;700&display=swap">
<style>
  :root {
    --navy: #233673;
    --red: #ee3338;
    --white: #ffffff;
    --page: #e4e4e4;
    --serif: "Alegreya", Georgia, serif;
  }
  * { box-sizing: border-box; margin: 0; padding: 0; }
  html, body {
    width: 1125px; height: 1200px; overflow: hidden;
    background: var(--page);
    font-family: var(--serif);
  }
  .card {
    position: absolute; left: 150px;
    width: 826px; height: 470px;
    overflow: hidden;
  }
  .card--front { top: 98px; background: var(--navy); }
  .card--back { top: 630px; background: var(--white); }

  .stripe-band {
    position: absolute; left: 0; width: 100%;
    background: var(--red);
  }
  .stripe-band--top { top: 0; height: 86px; }
  .stripe-band--bottom { bottom: 0; height: 66px; }
  .stripe-line {
    position: absolute; left: 0; width: 100%; height: 3px;
    background: var(--white);
  }

  .contact {
    position: absolute; top: 86px; left: 0; width: 100%; height: 318px;
    text-align: center; color: var(--white);
  }
  .contact__name {
    margin-top: 48px;
    font-size: 32px; font-weight: 700; letter-spacing: 1px;
    text-transform: uppercase;
  }
  .contact__rule {
    width: 195px; height: 2px; background: var(--white);
    margin: 20px auto 26px;
  }
  .contact__line {
    font-size: 21px; line-height: 27px;
    display: flex; align-items: center; justify-content: center; gap: 8px;
  }
  .contact__line svg { fill: var(--white); flex: none; }
  .contact__address { margin-top: 16px; font-size: 21px; line-height: 25px; }

  .brand {
    position: absolute; inset: 0;
    display: flex; align-items: center; justify-content: center; gap: 16px;
  }
  .brand__dot {
    width: 54px; height: 54px; border-radius: 50%; background: var(--navy);
  }
  .brand__name {
    font-size: 62px; font-weight: 700; color: var(--navy);
    text-transform: uppercase; letter-spacing: 1px;
  }
</style>
</head>
<body>
  <section class="card card--front">
    <div class="stripe-band stripe-band--top">
      <span class="stripe-line" style="top:26px"></span>
      <span class="stripe-line" style="top:57px"></span>
    </div>

    <div class="contact">
      <h1 class="contact__name">Faisal Qureshi</h1>
      <div class="contact__rule"></div>
      <p class="contact__line">
        <svg width="16" height="18" viewBox="0 0 24 24" aria-hidden="true"><path d="M6.6 10.8a15.1 15.1 0 0 0 6.6 6.6l2.2-2.2a1 1 0 0 1 1-.25 11.4 11.4 0 0 0 3.6.6 1 1 0 0 1 1 1V20a1 1 0 0 1-1 1A17 17 0 0 1 3 4a1 1 0 0 1 1-1h3.5a1 1 0 0 1 1 1c0 1.25.2 2.45.6 3.6a1 1 0 0 1-.25 1z"/></svg>
        413-719-4820
      </p>
      <p class="contact__line">
        <svg width="13" height="21" viewBox="0 0 13 21" aria-hidden="true"><path d="M2 0h9a2 2 0 0 1 2 2v17a2 2 0 0 1-2 2H2a2 2 0 0 1-2-2V2a2 2 0 0 1 2-2zm0 2.5v13.5h9V2.5z"/></svg>
        413-585-2046
      </p>
      <p class="contact__line">
        <svg width="15" height="11" viewBox="0 0 15 11" aria-hidden="true"><path d="M0 0h15v1.2L7.5 6 0 1.2zM0 2.8l7.5 4.8L15 2.8V11H0z"/></svg>
        Brooksidegrocer512@fernpost.com
      </p>
      <p class="contact__address">Ashford, MA on 512<br>Mill Pond Road &amp; 28 Elm St.</p>
    </div>

    <div class="stripe-band stripe-band--bottom">
      <span class="stripe-line" style="top:24px"></span>
      <span class="stripe-line" style="top:46px"></span>
    </div>
  </section>

  <section class="card card--back">
    <div class="brand">
      <span class="brand__dot"></span>
      <span class="brand__name">Brookside Grocer</span>
    </div>
  </section>
</body>
</html>
```